Project Meridel PowerPoint Design

This is a PPT design for Power & Utilities company who are in the process of a technology upgrade for their Finance department. We are looking to develop a branded PPT for Project Meridel (specifically MERIDEL). Why does Meridel resonate? "The Earth is pointed almost directly at Meridel. During the course of the night,
Meridel does not rise or set, but remains in nearly the same spot above the
northern horizon year- round while the other stars circle around it."
Meridel represents the guiding principles that manage, monitor and
control the organizations financials.

Target Market(s)

Finance stakeholders impacted by technology enhancement

Font styles to use
Serif
Other font styles liked:
• Arial

Colors
0054AA
0677BA
7BADD7
CADEEF
E8F1F8

Requirements
Must have
• Various slide layout ( Cover slide, content slide, divider, etc). Attached is the logo and corporate colors
Nice to have
• Over the top creativity

```html
<!DOCTYPE html>
<html lang="en">
<head>
<meta charset="utf-8">
<title>Project Meridel — Slide Deck</title>
<link href="https://fonts.googleapis.com/css2?family=Roboto:wght@300;400;500;700&display=swap" rel="stylesheet">
<style>
:root{
  --board:#8e9194;
  --navy:#0b1330;
  --brand:#2f5ec4;
  --accent:#2a47a5;
  --ink:#1b1b1b;
  --rule:#9a9a9a;
  --frame-blue:#8aa0d0;
  --frame-grey:#8d8d8d;
  --y1:#ff0000;--y2:#0a0a78;--y3:#ffb800;--y4:#990033;--y5:#ff8000;
}
*{margin:0;padding:0;box-sizing:border-box}
html,body{width:822px;height:1200px;overflow:hidden;background:var(--board)}
body{font-family:"Roboto",Arial,sans-serif;color:var(--ink)}
.board{position:relative;width:822px;height:1200px}
.slide{position:absolute;width:366px;height:259px;overflow:hidden;background:#fff}
.col-l{left:39px}.col-r{left:415px}
.row-1{top:46px}.row-2{top:332px}.row-3{top:606px}.row-4{top:891px}
.abs{position:absolute}
.fill{position:absolute;inset:0}

/* wordmark */
.wordmark{position:absolute;color:var(--brand);font-weight:500;line-height:1;text-transform:uppercase}
.wordmark .top{display:block}
.wordmark .main{display:block}

/* footer */
.footer-rule{position:absolute;left:0;top:244px;width:338px;height:1.5px;background:var(--rule)}
.footer-url{position:absolute;left:12px;top:249px;font-size:4.6px;color:#777;letter-spacing:.1px}
.page-no{position:absolute;left:337px;top:237px;width:15px;height:15px;border-radius:50%;background:#1f47a8;border:2px solid #fff;box-shadow:0 0 0 1px #9aa9cc;color:#fff;font-size:4.8px;font-weight:700;display:flex;align-items:center;justify-content:center}
.footer-badge{position:absolute;left:160px;top:238px;width:46px;height:12px;border-radius:50%;background:#0b0b14;display:flex;align-items:center;justify-content:center;font-size:5px;font-weight:500;color:var(--brand);letter-spacing:.4px}

/* headings */
.slide-title{position:absolute;left:12px;top:22px;border-left:1px solid var(--accent);padding-left:3px}
.slide-title h2{font-size:8.6px;font-weight:400;color:var(--accent);line-height:1.2}
.slide-title p{font-size:4.4px;color:#333;margin-top:2px}
.subhead{position:absolute;font-size:8.4px;color:var(--accent);font-weight:400}
.body-copy{position:absolute;font-size:4.6px;line-height:6.2px;text-align:justify;color:#222}

/* section dividers */
.sec-no{position:absolute;width:23px;height:23px;border-radius:50%;display:flex;align-items:center;justify-content:center;font-size:10px;font-weight:500}
.sec-title{position:absolute;font-size:11px;font-weight:300;letter-spacing:.2px}
.sec-text{position:absolute;font-size:4.8px;line-height:6.2px;width:160px}

/* services */
.svc-icon{position:absolute;width:38px;height:38px;border-radius:50%;background:#fff;display:flex;align-items:center;justify-content:center}
.svc{position:absolute;width:74px;text-align:center}
.svc h3{font-size:5.9px;font-weight:700;color:#222;margin-bottom:5px}
.svc p{font-size:6px;line-height:7.8px;color:#222}

/* timeline */
.tl-label{position:absolute;font-size:4.9px;line-height:6.2px;text-align:right;width:60px;color:#222}
.tl-stem{position:absolute;width:1.3px}
.tl-year{position:absolute;top:138px;height:26px;display:flex;align-items:center;justify-content:center;color:#fff;font-size:8.4px;font-weight:400}
</style>
</head>
<body>
<main class="board">

  <!-- Cover -->
  <section class="slide col-l row-1" style="background:#02040c">
    <div class="fill" role="img" aria-label="Starfield over a glowing blue digital horizon grid" style="background:radial-gradient(ellipse 70% 45% at 50% 100%,#1f8fff 0%,#0a3d8a 35%,rgba(2,6,20,0) 75%),linear-gradient(#03050d,#040a1c 70%,#0b3fa0 92%,#0a1c4a)"></div>
    <div class="wordmark" style="left:46px;top:78px;color:var(--brand)">
      <span class="top" style="font-size:24px;letter-spacing:9px;margin-left:118px">Project</span>
      <span class="main" style="font-size:50px;letter-spacing:4px;margin-top:4px">Meridel</span>
    </div>
  </section>

  <!-- Introduction -->
  <section class="slide col-r row-1">
    <svg class="fill" width="366" height="259" viewBox="0 0 366 259" role="img" aria-label="Team reviewing hand-written financial plans beside a laptop">
      <defs><linearGradient id="introPhoto" x1="0" y1="0" x2="1" y2="1"><stop offset="0" stop-color="#6f8e93"/><stop offset=".5" stop-color="#b9c9c7"/><stop offset="1" stop-color="#8a7466"/></linearGradient></defs>
      <path d="M0 0H366V162Q183 70 0 148Z" fill="url(#introPhoto)"/>
      <path d="M0 148Q183 70 366 162" fill="none" stroke="#2b56c0" stroke-width="3"/>
    </svg>
    <div class="abs" style="left:127px;top:97px;width:112px;height:35px;border-radius:50%;background:#0b0b14"></div>
    <div class="wordmark" style="left:127px;top:104px;width:112px;text-align:center">
      <span class="top" style="font-size:6px;letter-spacing:2px">Project</span>
      <span class="main" style="font-size:13px;letter-spacing:1px;margin-top:1px">Meridel</span>
    </div>
    <h1 class="abs" style="left:0;width:366px;top:151px;text-align:center;font-size:10.5px;font-weight:700;color:#222">INTRODUCTION</h1>
    <p class="abs" style="left:19px;width:330px;top:170px;font-size:6.3px;line-height:7.8px">Lorem ipsum dolor sit amet, consectetur adipiscing elit, sed do eiusmod tempor incididunt ut labore et dolore magna aliqua. Quis ipsum suspendisse ultrices gravida. Risus commodo viverra maecenas accumsan lacus vel facilisis.</p>
    <p class="abs" style="left:19px;width:330px;top:202px;font-size:6.3px;line-height:7.8px">Lorem ipsum dolor sit amet, consectetur adipiscing elit, sed do eiusmod tempor incididunt ut labore et dolore magna aliqua. Quis ipsum suspendisse ultrices gravida. Risus commodo viverra maecenas accumsan lacus vel facilisis.</p>
    <div class="footer-rule"></div>
    <div class="footer-url">WWW.PROJECTMERIDEL.COM</div>
    <div class="page-no">1</div>
  </section>

  <!-- Section 01 -->
  <section class="slide col-l row-2" style="background:#000">
    <div class="fill" role="img" aria-label="Dark starry sky above the curved edge of the Earth" style="background:radial-gradient(ellipse 80% 30% at 50% 100%,#2d4a6a 0%,#0d1a2a 55%,rgba(0,0,0,0) 80%),#020306"></div>
    <div class="sec-no" style="left:32px;top:102px;border:1px solid #fff;color:#fff">01</div>
    <div class="sec-title" style="left:63px;top:106px;color:#fff">SECTION TITLE</div>
    <p class="sec-text" style="left:63px;top:122px;color:#fff">Lorem Ipsum is simply dummy text of the printing and typesetting industry.Lorem Ipsum is simply dummy text of the printing and typesetting industry.</p>
    <div class="wordmark" style="left:240px;top:111px">
      <span class="top" style="font-size:7.5px;letter-spacing:3px;margin-left:36px">Project</span>
      <span class="main" style="font-size:16px;letter-spacing:2px;margin-top:1px">Meridel</span>
    </div>
  </section>

  <!-- Our services -->
  <section class="slide col-r row-2">
    <svg class="fill" width="366" height="259" viewBox="0 0 366 259" role="img" aria-label="Hand touching a glowing financial chart dashboard with market figures">
      <defs><linearGradient id="svcPhoto" x1="0" y1="0" x2="1" y2="0"><stop offset="0" stop-color="#0f3b55"/><stop offset=".38" stop-color="#c86a3a"/><stop offset=".6" stop-color="#1c5e7a"/><stop offset="1" stop-color="#12384f"/></linearGradient></defs>
      <path d="M0 0H366V162Q183 75 0 150Z" fill="url(#svcPhoto)"/>
      <path d="M0 150Q183 75 366 162" fill="none" stroke="#2b56c0" stroke-width="3"/>
    </svg>
    <div class="abs" style="left:13px;top:9px;width:1px;height:16px;background:#fff"></div>
    <div class="abs" style="left:17px;top:11px;font-size:8px;color:#fff">OUR SERVICES</div>

    <div class="svc-icon" style="left:28px;top:114px">
      <svg width="18" height="16" viewBox="0 0 18 16" fill="none" stroke="#333" stroke-width=".9"><path d="M1 15H17M3 15V10H6V15M8 15V7H11V15M13 15V9H16V15M2 8L7 4L10 6L16 1M13 1H16V4"/></svg>
    </div>
    <div class="svc-icon" style="left:120px;top:91px">
      <svg width="16" height="16" viewBox="0 0 16 16" fill="none" stroke="#333" stroke-width=".9"><rect x="1" y="2" width="14" height="9"/><path d="M6 14H10M8 11V14"/><circle cx="8" cy="6" r="2.2"/><path d="M7 8.5H9"/></svg>
    </div>
    <div class="svc-icon" style="left:200px;top:91px">
      <svg width="16" height="16" viewBox="0 0 16 16" fill="none" stroke="#333" stroke-width=".9"><circle cx="8" cy="5" r="3"/><path d="M2 15C2 11 5 9.5 8 9.5S14 11 14 15ZM8 9.5V13"/></svg>
    </div>
    <div class="svc-icon" style="left:298px;top:116px">
      <svg width="18" height="16" viewBox="0 0 18 16" fill="none" stroke="#333" stroke-width=".9"><circle cx="9" cy="3.5" r="2.5"/><circle cx="4" cy="9" r="1.6"/><circle cx="9" cy="9" r="1.6"/><circle cx="14" cy="9" r="1.6"/><path d="M1.5 15C1.5 12 6.5 12 6.5 15M6.5 15C6.5 12 11.5 12 11.5 15M11.5 15C11.5 12 16.5 12 16.5 15"/></svg>
    </div>

    <div class="svc" style="left:10px;top:153px"><h3>HEADING1</h3><p>Lorem ipsum dolor sit amet, consectetur adipiscing elit, sed do eiusmod tempor incididunt ut labore et dolore magna aliqua. Quis ipsum</p></div>
    <div class="svc" style="left:100px;top:148px"><h3>HEADING2</h3><p>Lorem ipsum dolor sit amet, consectetur adipiscing elit, sed do eiusmod tempor incididunt ut labore et dolore magna aliqua. Quis ipsum suspendisse ultrices gravida. Risus</p></div>
    <div class="svc" style="left:185px;top:148px"><h3>HEADING3</h3><p>Lorem ipsum dolor sit amet, consectetur adipiscing elit, sed do eiusmod tempor incididunt ut labore et dolore magna aliqua. Quis ipsum suspendisse ultrices</p></div>
    <div class="svc" style="left:279px;top:159px"><h3 style="margin-left:12px">HEADING4</h3><p>Lorem ipsum dolor sit amet, consectetur adipiscing elit, sed do eiusmod tempor incididunt ut labore et dolore magna</p></div>

    <div class="footer-rule"></div>
    <div class="footer-badge">MERIDEL</div>
    <div class="footer-url">WWW.PROJECTMERIDEL.COM</div>
    <div class="page-no">2</div>
  </section>

  <!-- Image left -->
  <section class="slide col-l row-3">
    <div class="slide-title"><h2>Image at left with the text</h2><p>subtitle goes here</p></div>
    <div class="abs" style="left:0;top:65px;width:25px;height:143px;background:var(--frame-blue)"></div>
    <div class="abs" style="left:139px;top:65px;width:41px;height:143px;background:var(--frame-grey)"></div>
    <div class="abs" role="img" aria-label="Businessman holding a tablet with a glowing rising bar chart" style="left:0;top:68px;width:178px;height:136px;background:radial-gradient(ellipse 50% 40% at 50% 55%,#2fd6c0 0%,#1e6d6a 50%,#24403f 100%)"></div>
    <div class="subhead" style="left:198px;top:79px">Subtitle here</div>
    <p class="body-copy" style="left:198px;top:98px;width:136px">Lorem ipsum dolor sit amet, consectetur adipiscing elit, sed do eiusmod tempor incididunt ut labore et dolore magna aliqua. Quis ipsum suspendisse ultrices gravida. Risus commodo viverra maecenas accumsan lacus vel facilisis.<br>Lorem ipsum dolor sit amet, consectetur adipiscing elit, sed do eiusmod tempor incididunt ut labore et dolore magna aliqua. Quis ipsum suspendisse ultrices gravida. Risus commodo viverra maecenas accumsan lacus vel facilisis.<br>Lorem ipsum dolor sit amet, consectetur adipiscing elit, sed do eiusmod tempor incididunt ut labore et dolore magna aliqua. Quis ipsum suspendisse ultrices gravida. Risus commodo viverra maecenas accumsan lacus vel facilisis.</p>
    <div class="footer-rule"></div>
    <div class="footer-badge">MERIDEL</div>
    <div class="footer-url">WWW.PROJECTMERIDEL.COM</div>
    <div class="page-no">3</div>
  </section>

  <!-- Section 02 -->
  <section class="slide col-r row-3">
    <div class="fill" role="img" aria-label="Looking up at tall glass office towers against a pale sky" style="background:linear-gradient(110deg,#f4f4f4 0%,#ededed 45%,#d2d2d2 70%,#f2f2f2 100%)"></div>
    <div class="wordmark" style="left:58px;top:41px">
      <span class="top" style="font-size:7.5px;letter-spacing:3px;margin-left:36px">Project</span>
      <span class="main" style="font-size:16px;letter-spacing:2px;margin-top:1px">Meridel</span>
    </div>
    <div class="sec-no" style="left:28px;top:69px;border:1px solid #111;color:#111">02</div>
    <div class="sec-title" style="left:58px;top:73px;color:#111">SECTION TITLE</div>
    <p class="sec-text" style="left:59px;top:90px;color:#111">Lorem Ipsum is simply dummy text of the printing and typesetting industry.Lorem Ipsum is simply dummy text of the printing and typesetting industry.</p>
  </section>

  <!-- Image right -->
  <section class="slide col-l row-4">
    <div class="slide-title"><h2>Image at right with the text</h2><p>subtitle goes here</p></div>
    <div class="subhead" style="left:11px;top:79px">Subtitle here</div>
    <p class="body-copy" style="left:12px;top:97px;width:136px">Lorem ipsum dolor sit amet, consectetur adipiscing elit, sed do eiusmod tempor incididunt ut labore et dolore magna aliqua. Quis ipsum suspendisse ultrices gravida. Risus commodo viverra maecenas accumsan lacus vel facilisis.<br>Lorem ipsum dolor sit amet, consectetur adipiscing elit, sed do eiusmod tempor incididunt ut labore et dolore magna aliqua. Quis ipsum suspendisse ultrices gravida. Risus commodo viverra maecenas accumsan lacus vel facilisis.<br>Lorem ipsum dolor sit amet, consectetur adipiscing elit, sed do eiusmod tempor incididunt ut labore et dolore magna aliqua. Quis ipsum suspendisse ultrices gravida. Risus commodo viverra maecenas accumsan lacus vel facilisis.</p>
    <div class="abs" style="left:174px;top:66px;width:40px;height:143px;background:var(--frame-blue)"></div>
    <div class="abs" style="left:328px;top:66px;width:38px;height:143px;background:var(--frame-grey)"></div>
    <div class="abs" role="img" aria-label="Colleagues meeting around a wooden table with laptops" style="left:177px;top:69px;width:189px;height:136px;background:linear-gradient(160deg,#6d6a66 0%,#3a3532 45%,#8a5a36 75%,#2a2624 100%)"></div>
    <div class="footer-rule"></div>
    <div class="footer-badge">MERIDEL</div>
    <div class="footer-url">WWW.PROJECTMERIDEL.COM</div>
    <div class="page-no">5</div>
  </section>

  <!-- Timeline -->
  <section class="slide col-r row-4">
    <div class="slide-title" style="top:25px"><h2 style="padding:2px 0">Timeline Infographics</h2></div>

    <div class="tl-label" style="left:10px;top:76px">Lorem ipsum dolor sit amet, consectetur</div>
    <div class="tl-stem" style="left:72px;top:75px;height:64px;background:var(--y1)"></div>
    <div class="tl-label" style="left:138px;top:76px">Lorem ipsum dolor sit amet, consectetur</div>
    <div class="tl-stem" style="left:200px;top:75px;height:64px;background:var(--y3)"></div>
    <div class="tl-label" style="left:265px;top:76px">Lorem ipsum dolor sit amet, consectetur</div>
    <div class="tl-stem" style="left:327px;top:75px;height:64px;background:var(--y5)"></div>

    <div class="tl-stem" style="left:137px;top:163px;height:41px;background:var(--y2)"></div>
    <div class="tl-label" style="left:74px;top:161px">Lorem ipsum dolor sit amet, consectetur</div>
    <div class="tl-stem" style="left:264px;top:163px;height:41px;background:var(--y4)"></div>
    <div class="tl-label" style="left:201px;top:161px">Lorem ipsum dolor sit amet, consectetur</div>

    <svg class="abs" style="left:0;top:138px" width="366" height="26" viewBox="0 0 366 26">
      <path d="M24 0H72A13 13 0 0 1 72 26H24Z" fill="var(--y1)"/>
      <path d="M88 0H136A13 13 0 0 1 136 26H88A13 13 0 0 0 88 0Z" fill="var(--y2)"/>
      <path d="M151 0H199A13 13 0 0 1 199 26H151A13 13 0 0 0 151 0Z" fill="var(--y3)"/>
      <path d="M215 0H263A13 13 0 0 1 263 26H215A13 13 0 0 0 215 0Z" fill="var(--y4)"/>
      <path d="M279 0H327A13 13 0 0 1 327 26H279A13 13 0 0 0 279 0Z" fill="var(--y5)"/>
    </svg>
    <div class="tl-year" style="left:24px;width:61px">YEAR1</div>
    <div class="tl-year" style="left:88px;width:61px">YEAR2</div>
    <div class="tl-year" style="left:151px;width:61px">YEAR3</div>
    <div class="tl-year" style="left:215px;width:61px">YEAR4</div>
    <div class="tl-year" style="left:279px;width:61px">YEAR5</div>

    <div class="footer-rule"></div>
    <div class="footer-badge">MERIDEL</div>
    <div class="footer-url">WWW.PROJECTMERIDEL.COM</div>
    <div class="page-no">4</div>
  </section>

</main>
</body>
</html>
```